Business Card Design and Stationary design for consulting firm

Harbourline Sourcing are looking for a new business card design and a design for their A4 letterhead / A4 invoices.

We are seeking to heavily increase our brand awareness and require a business card that's professional in appearance but also shows flare and innovation. A card design that people will remember.

About Us
Harbourline Sourcing are `The Sourcing Crew’.
Our mission is to be one of Australia’s greatest companies. Our aim is to help our customers achieve the best result from their purchasing experience.

Our Requirement:
• IMPACT! IMPACT! IMPACT!
• BUSINESS & PROFESSIONAL LOOKING

• Our business colours are orange, blue and green (See the logo attached).

We have provided an Art Design specification (attached) that needs to be followed for you to win the design. This also has the font, which is used on the logo.

We are after a two sided business card

Side One should have the:
The company Logo
The Sourcing Crew
www.harbourlinesourcing.com.au
Procure | Personnel | Probity & Privacy
Sydney | Melbourne | Adelaide | Brisbane

Side Two
Logo (optional)
Harbourline Sourcing (optional)
Employee details (details listed below)

The above format is our preferred option, but if you think you can come up with something better, feel free to put it forward.

We are leaving the design up to you, but it must incorporate the logo.

We will need a template that we can change the employee details on, as we will be adding more staff over the coming months.

The details below are for one employee per card with the same design.
------------------------

Employee Details:

Marcus Del Arroyo MBA, MMgmtStratProc
Principal Consultant
0491 372 618
Marcus@harbourlinesourcing.com.au

Brianna Tolley
Consulting Manager
0462 915 308
Brianna@harbourlinesourcing.com.au

Our website is www.harbourlinesourcing.com.au

The Letterhead / invoice needs to incorporate:
the company Logo
The Sourcing Crew
Sydney | Melbourne | Adelaide | Brisbane but otherwise the design is over to you.

This file needs to be delivered in word format as other detail will be added to the documents.

We look forward to you award winning designs. If you require any further information please feel free to contact us.

Regards
Harbourline Sourcing

Target Market(s)

Our Target market is companies with 80+ employees. The market we segment is heavily male based, between the ages of 35-55 years of age.

Industry/Entity Type

Consulting

Contact Information for Business Card

See Project Description

Font styles to use
Other font styles liked:
• See Art Specification

Requirements
Must have
• Company Colours, See Project Description
Should not have
• Be outside the Art specification guidelines

```html
<!DOCTYPE html>
<html lang="en">
<head>
<meta charset="utf-8">
<title>Harbourline Sourcing – Stationery Set</title>
<link rel="stylesheet" href="https://fonts.googleapis.com/css2?family=Open+Sans:wght@400;600;700&display=swap">
<style>
  :root {
    --board: #b5a68b;
    --paper: #e7e7e7;
    --ink: #333333;
    --charcoal: #3d3d3d;
    --flap: #050505;
    --brand-orange: #f08a2c;
    --brand-blue: #2a8fd6;
    --brand-green: #6cbf3a;
    --name-blue: #1d4f8f;
    --title-orange: #d0611e;
    --icon-blue: #2a7fd0;
  }
  * { margin: 0; padding: 0; box-sizing: border-box; }
  html, body { width: 1200px; height: 644px; overflow: hidden; }
  body {
    position: relative;
    background: var(--board);
    font-family: "Open Sans", Arial, sans-serif;
    color: var(--ink);
  }
  .sheet { position: absolute; background: var(--paper); box-shadow: 0 1px 3px rgba(0,0,0,.25); }

  .wordmark { position: absolute; display: flex; flex-direction: column; align-items: center; }
  .wordmark .dot { border-radius: 50%; background: var(--ink); }
  .wordmark .name {
    font-weight: 700; color: var(--ink); text-transform: uppercase;
    text-align: center; line-height: 1.1; letter-spacing: .04em;
  }

  .hero-mark { left: 42px; top: 300px; width: 180px; }
  .hero-mark .dot { width: 46px; height: 46px; margin-bottom: 18px; }
  .hero-mark .name { font-size: 22px; }

  .card-backdrop {
    position: absolute; left: 0; top: 430px; width: 266px; height: 214px;
    background: radial-gradient(ellipse at 40% 40%, #e4ddd2 0%, #cbbfae 55%, rgba(181,166,139,0) 100%);
  }

  .business-card {
    position: absolute; left: 19px; top: 466px; width: 221px; height: 127px;
    background: rgba(245,245,245,.85); box-shadow: 0 1px 3px rgba(0,0,0,.3);
  }
  .business-card .wordmark { left: 6px; top: 18px; width: 76px; }
  .business-card .dot { width: 14px; height: 14px; margin-bottom: 6px; }
  .business-card .name { font-size: 9px; }
  .business-card .tagline {
    position: absolute; left: 4px; top: 77px; width: 80px; text-align: center;
    font-size: 5.5px; font-weight: 700; color: var(--icon-blue);
  }
  .business-card .divider { position: absolute; left: 91px; top: 12px; width: 1px; height: 76px; background: #9a9a9a; }
  .business-card .details { position: absolute; left: 101px; top: 12px; }
  .person-name { font-size: 8.5px; font-weight: 700; color: var(--name-blue); line-height: 1.2; }
  .person-cred { font-size: 6.5px; font-weight: 700; color: var(--name-blue); line-height: 1.2; }
  .person-role { font-size: 6.5px; color: var(--title-orange); line-height: 1.3; margin-bottom: 4px; }
  .contact-line { display: flex; align-items: center; gap: 3px; font-size: 5.6px; line-height: 1.55; }
  .contact-line svg { flex: none; }

  .footer-band { position: absolute; left: 0; bottom: 0; width: 100%; background: var(--charcoal); }
  .footer-text { position: absolute; left: 0; top: 0; color: #fff; white-space: nowrap; }
  .footer-text .sep { color: var(--brand-orange); }
  .accent-strip {
    position: absolute; right: 0;
    background: linear-gradient(90deg, var(--brand-orange), var(--brand-blue) 50%, var(--brand-green));
  }
  .business-card .footer-band { height: 20px; }
  .business-card .footer-text { left: 9px; top: 2px; font-size: 5.8px; line-height: 1.35; }
  .business-card .accent-strip { top: 6px; width: 66px; height: 6px; }

  .letterhead { left: 266px; top: 27px; width: 403px; height: 571px; }
  .letterhead .wordmark { left: 20px; top: 32px; width: 72px; }
  .letterhead .dot, .envelope-front .dot { width: 18px; height: 18px; margin-bottom: 8px; }
  .letterhead .name, .envelope-front .name { font-size: 9px; }
  .letterhead .contacts { position: absolute; left: 240px; top: 37px; }
  .letterhead .contact-line { font-size: 7.4px; line-height: 1.75; }
  .letterhead .footer-band, .envelope-front .footer-band { height: 25px; }
  .letterhead .footer-text { left: 25px; top: 2px; font-size: 7.4px; line-height: 1.35; }
  .letterhead .accent-strip { top: 8px; width: 130px; height: 10px; }

  .envelope-back { left: 684px; top: 150px; width: 478px; height: 216px; }
  .envelope-back .flap { position: absolute; left: 0; top: 0; width: 100%; height: 80px; }
  .envelope-back .wordmark { left: 189px; top: 20px; width: 100px; }
  .envelope-back .dot { width: 20px; height: 20px; margin-bottom: 7px; background: #fff; }
  .envelope-back .name { font-size: 9px; color: #fff; }

  .envelope-front { left: 685px; top: 386px; width: 477px; height: 215px; }
  .envelope-front .wordmark { left: 20px; top: 10px; width: 76px; }
  .envelope-front .accent-strip { top: 8px; width: 215px; height: 10px; }
</style>
</head>
<body>

  <div class="wordmark hero-mark">
    <span class="dot"></span>
    <span class="name">Harbourline<br>Sourcing</span>
  </div>

  <div class="card-backdrop" role="img" aria-label="Softly blurred office interior behind the business card"></div>

  <section class="business-card">
    <div class="wordmark">
      <span class="dot"></span>
      <span class="name">Harbourline<br>Sourcing</span>
    </div>
    <p class="tagline">The Sourcing Crew</p>
    <span class="divider"></span>
    <div class="details">
      <p class="person-name">Marcus Del Arroyo</p>
      <p class="person-cred">MBA, MMgmtStratProc</p>
      <p class="person-role">Principal Consultant</p>
      <p class="contact-line"><svg width="5" height="6" viewBox="0 0 5 6"><rect x=".5" y=".3" width="4" height="5.4" rx=".6" fill="none" stroke="#333" stroke-width=".7"/></svg>0491 372 618</p>
      <p class="contact-line"><svg width="6" height="5" viewBox="0 0 6 5"><rect width="6" height="4.4" y=".3" fill="var(--icon-blue)"/><path d="M0 .4 3 2.6 6 .4" fill="none" stroke="#fff" stroke-width=".5"/></svg>Marcus@harbourlinesourcing.com.au</p>
      <p class="contact-line"><svg width="5" height="5" viewBox="0 0 5 5"><circle cx="2.5" cy="2.5" r="2.5" fill="#333"/></svg>www.harbourlinesourcing.com.au</p>
    </div>
    <div class="footer-band">
      <p class="footer-text">Procure <span class="sep">|</span> Personnel <span class="sep">|</span> Probity &amp; Privacy<br>Sydney <span class="sep">|</span> Melbourne <span class="sep">|</span> Adelaide <span class="sep">|</span> Brisbane</p>
      <div class="accent-strip" role="img" aria-label="Brand colour accent in orange, blue and green"></div>
    </div>
  </section>

  <section class="sheet letterhead">
    <div class="wordmark">
      <span class="dot"></span>
      <span class="name">Harbourline<br>Sourcing</span>
    </div>
    <div class="contacts">
      <p class="contact-line"><svg width="7" height="9" viewBox="0 0 7 9"><rect x=".6" y=".5" width="5.8" height="8" rx=".8" fill="none" stroke="var(--icon-blue)" stroke-width="1"/></svg>0491 372 618</p>
      <p class="contact-line"><svg width="8" height="7" viewBox="0 0 8 7"><rect width="8" height="6" y=".5" fill="var(--icon-blue)"/><path d="M0 .6 4 3.6 8 .6" fill="none" stroke="#fff" stroke-width=".7"/></svg>Marcus@harbourlinesourcing.com.au</p>
      <p class="contact-line"><svg width="8" height="8" viewBox="0 0 8 8"><circle cx="4" cy="4" r="4" fill="var(--icon-blue)"/></svg>harbourlinesourcing.com.au</p>
    </div>
    <div class="footer-band">
      <p class="footer-text">Procure <span class="sep">|</span> Personnel <span class="sep">|</span> Probity &amp; Privacy<br>Sydney <span class="sep">|</span> Melbourne <span class="sep">|</span> Adelaide <span class="sep">|</span> Brisbane</p>
      <div class="accent-strip" role="img" aria-label="Brand colour accent in orange, blue and green"></div>
    </div>
  </section>

  <section class="sheet envelope-back">
    <svg class="flap" viewBox="0 0 478 80" preserveAspectRatio="none">
      <path d="M0 0 H478 L462 58 Q457 80 435 80 H43 Q21 80 16 58 Z" fill="var(--flap)"/>
    </svg>
    <div class="wordmark">
      <span class="dot"></span>
      <span class="name">Harbourline Sourcing</span>
    </div>
  </section>

  <section class="sheet envelope-front">
    <div class="wordmark">
      <span class="dot"></span>
      <span class="name">Harbourline<br>Sourcing</span>
    </div>
    <div class="footer-band">
      <div class="accent-strip" role="img" aria-label="Brand colour accent in orange, blue and green"></div>
    </div>
  </section>

</body>
</html>
```